Redesign start page for existing online shop

We are selling building material (chimneys and flue pipes) as well as fireplaces (stoves). For this online shop we need a new start page. The domain is kaminwelt-versand.de. Here you can see the current design. We want a smoother design with just one banner in the middle instead of the three in the first row. The look has to be more professional and trustworthy. You can therefore play with the colors. We want to try some different orange instead of our yellow / orange color. A few more things: - The phone number has to be bigger and more highlighted - So the 5 advantages at the top should be shown in a different way - New design for the products below - New footer

Target Market(s)

Germany and other countries in Europe.

Industry/Entity Type

Home Builder

Number of Pages Required

1 page

Font styles to use
Other font styles liked:
• Please se the font on our current site.

Colors
f78f20
f68d4c

Requirements
Must have
• - Clear design - Trustworthy look - All elements Which are now shown shoulderstand be still there after redesigning -
Nice to have
• - See the Following sites to have a clou about our wishes: glutvia.de warmbrio.de

```html
<!DOCTYPE html>
<html lang="en">
<head>
<meta charset="utf-8">
<title>Kaminwelt Versand – Stainless Steel Chimneys</title>
<link href="https://fonts.googleapis.com/css2?family=Open+Sans:wght@400;600;700;800&display=swap" rel="stylesheet">
<style>
:root{
  --orange:#f78f20;
  --orange-soft:#f68d4c;
  --dark:#2f2f2f;
  --darker:#262626;
  --text:#444;
  --muted:#777;
  --light:#efefef;
  --line:#e2e2e2;
  --white:#fff;
}
*{box-sizing:border-box;margin:0;padding:0}
html,body{width:1200px;height:3543px;overflow:hidden}
body{font-family:"Open Sans",Arial,sans-serif;color:var(--text);background:var(--white);position:relative}
a{color:inherit;text-decoration:none}

.topbar{height:42px;background:var(--dark);color:#ddd;font-size:11px;font-weight:600;display:flex;align-items:center;padding:0 100px;justify-content:space-between}
.topbar .links span{margin-right:22px}
.topbar .rating{color:#fff}
.topbar .rating b{color:#f4c21b;letter-spacing:1px;margin-right:6px}
.topbar .account{display:flex;height:42px}
.topbar .account span{background:#555;padding:0 16px;display:flex;align-items:center}
.topbar .account span+span{background:#444}

.header{height:100px;display:flex;align-items:center;padding:0 100px;position:relative}
.brand{display:flex;align-items:center;gap:14px}
.brand .mark{width:52px;height:52px;border-radius:50%;border:4px solid var(--orange);flex:none}
.brand .name{font-size:25px;font-weight:800;line-height:1.05;color:#333;text-transform:uppercase}
.brand.light .name{color:#fff}
.seals{position:absolute;left:650px;top:22px;display:flex;gap:16px}
.seals i{display:block;width:48px;height:56px;background:#e8e8e8;border-radius:50%}
.seals i+i{border-radius:4px;background:#f3f3f3;border:2px solid #ddd}
.hotline{margin-left:auto;display:flex;align-items:center;gap:14px}
.hotline .ico{width:48px;height:48px;border-radius:50%;background:var(--orange);display:flex;align-items:center;justify-content:center}
.hotline strong{display:block;font-size:30px;font-weight:800;color:var(--orange);line-height:1}
.hotline small{font-size:11px;color:var(--muted);font-weight:600}

.nav{height:56px;border-top:1px solid var(--line);border-bottom:1px solid var(--line);display:flex;padding:0 100px}
.nav a{flex:1;display:flex;align-items:center;justify-content:center;font-size:13px;font-weight:700;color:#333;border-right:1px solid var(--line);text-transform:uppercase}
.nav a:first-child{border-left:1px solid var(--line)}

.perks{height:57px;background:var(--orange);display:flex;align-items:center;padding:0 100px;gap:60px;color:#fff;font-weight:600;font-size:15px;position:relative}
.perks span{display:flex;align-items:center;gap:12px}
.award{position:absolute;right:100px;top:-2px;width:120px;height:148px;background:#fff;box-shadow:0 2px 8px rgba(0,0,0,.2);padding:6px;z-index:3}
.award div{width:100%;height:100%;background:linear-gradient(135deg,#3a3a3a,#7a6a5a 60%,#cfc6bb)}

.hero{height:406px;background:linear-gradient(90deg,#cfd2d3,#8c8f91 40%,#6d7072 60%,#c9cbcc);position:relative;text-align:center;color:#fff}
.hero h1{padding-top:100px;font-size:52px;font-weight:800;letter-spacing:1px;line-height:1.25;text-shadow:0 2px 6px rgba(0,0,0,.35)}
.hero p{font-size:22px;font-weight:600;line-height:1.35;text-shadow:0 1px 4px rgba(0,0,0,.35)}
.btn{display:inline-block;background:var(--orange);color:#fff;font-weight:700;font-size:13px;text-transform:uppercase;padding:14px 26px}
.hero .btn{margin-top:22px;font-size:15px;padding:16px 30px}
.arrow{position:absolute;top:180px;width:48px;height:48px;border-radius:50%;background:rgba(255,255,255,.35);display:flex;align-items:center;justify-content:center}

.partners{height:102px;background:#c9c9c9;display:flex;align-items:center;justify-content:center;gap:120px;color:#fff;font-size:32px;font-weight:800}
.partners span{display:flex;align-items:center;gap:12px}
.partners i{width:22px;height:22px;background:#fff;display:block}

.features{height:331px;display:flex;padding:50px 100px 0;gap:30px;text-align:center}
.feature{flex:1}
.feature .circle{width:94px;height:94px;border-radius:50%;background:var(--orange);margin:0 auto 20px;display:flex;align-items:center;justify-content:center;box-shadow:0 0 0 5px #fde4c8}
.feature h3{font-size:17px;font-weight:600;color:#333;line-height:1.35;margin-bottom:10px}
.feature p{font-size:12px;color:var(--muted);line-height:1.55}

.how{height:482px;background:linear-gradient(135deg,rgba(247,143,32,.92),rgba(246,141,76,.85)),linear-gradient(90deg,#c8a27c,#efe0cc);color:#fff;text-align:center;position:relative}
.how h2{padding-top:50px;font-size:27px;font-weight:700}
.how .sub{font-size:15px;font-weight:600;margin-top:4px}
.steps{position:absolute;top:156px;left:95px;right:95px;display:flex;justify-content:space-between}
.steps::before{content:"";position:absolute;top:58px;left:120px;right:120px;height:3px;background:#fff}
.step{width:240px;position:relative}
.step .ring{width:118px;height:118px;border:4px solid #fff;border-radius:50%;margin:0 auto;display:flex;align-items:center;justify-content:center;background:var(--orange);position:relative}
.step .num{position:absolute;right:-8px;top:-8px;width:34px;height:34px;border-radius:50%;background:#fff;color:var(--orange);font-weight:700;font-size:15px;display:flex;align-items:center;justify-content:center}
.step p{margin-top:20px;font-size:17px;font-weight:600;line-height:1.3}
.how .cta{position:absolute;top:378px;left:0;right:0;display:flex;justify-content:center;align-items:center;gap:40px;font-size:24px;font-weight:600}
.how .cta .btn{background:#fff;color:#333;font-size:14px;padding:14px 28px}

.products{height:609px;padding:40px 87px 0;position:relative}
.products h2{text-align:center;font-size:25px;font-weight:700;color:#222;margin-bottom:28px}
.grid{display:flex;gap:15px}
.card{width:243px}
.card .img{height:250px}
.card h3{font-size:17px;font-weight:700;color:#222;margin-top:22px}
.card p{font-size:12px;color:var(--muted);line-height:1.5;margin-top:6px;height:54px}
.card .price{font-size:19px;font-weight:700;color:var(--orange);margin-top:8px}
.card .btn{margin-top:8px;width:134px;text-align:center;padding:9px 0}
.round{position:absolute;top:212px;width:40px;height:40px;border-radius:50%;border:1px solid #ddd;display:flex;align-items:center;justify-content:center;background:#fff}

.seo{background:var(--light);height:1082px;padding:40px 100px 0;font-size:11px;line-height:1.7;color:#666}
.seo h2{font-size:17px;color:var(--orange);font-weight:700;line-height:1.4;margin-bottom:14px}
.seo h3{font-size:14px;color:#333;font-weight:600;margin:22px 0 12px}
.seo p{margin-bottom:12px}

.footer{height:276px;background:var(--darker);border-top:5px solid var(--orange);color:#ccc;position:relative}
.footer .cols{display:flex;padding:24px 100px 0}
.footer .brand{margin-top:56px;width:325px}
.footer h4{color:#fff;font-size:14px;font-weight:700;text-transform:uppercase;margin-bottom:12px}
.footer ul{list-style:none;font-size:12px;line-height:1.55}
.col-info{width:170px}
.col-news{width:305px}
.col-news p{font-size:12px;line-height:1.5;color:#fff}
.col-news .field{margin-top:14px;width:255px;height:36px;background:#fff;color:#999;font-size:11px;padding:10px 12px}
.col-news .btn{margin-top:12px;padding:8px 14px;font-size:11px}
.col-contact li{display:flex;gap:10px;margin-bottom:4px}
.col-contact svg{flex:none;margin-top:3px}
.bottom{position:absolute;left:0;right:0;bottom:0;height:48px;background:#1e1e1e;display:flex;align-items:center;padding:0 100px;font-size:11px;color:#999}
.pay{margin-left:auto;display:flex;gap:8px}
.pay span{background:#fff;color:#444;font-size:10px;font-weight:700;padding:6px 8px;border-radius:3px}
.social{display:flex;gap:10px;margin-left:18px}
.social i{width:16px;height:16px;border-radius:50%;background:#fff;display:block}
</style>
</head>
<body>

<div class="topbar">
  <div class="links"><span>SHOPPING SAFELY ▾</span><span>ADVANTAGES ▾</span><span>CONSULTING &amp; CONTACT ▾</span></div>
  <div class="rating"><b>★★★★★</b>VERY GOOD(4.80/5.00)</div>
  <div class="account"><span>MY ACCOUNT</span><span>CART(0)</span></div>
</div>

<header class="header">
  <div class="brand"><span class="mark"></span><span class="name">Kaminwelt<br>Versand</span></div>
  <div class="seals"><i></i><i></i></div>
  <div class="hotline">
    <span class="ico"><svg width="24" height="24" viewBox="0 0 24 24"><path fill="#fff" d="M6.6 10.8a15 15 0 0 0 6.6 6.6l2.2-2.2c.3-.3.7-.4 1-.2 1.1.4 2.3.6 3.6.6.6 0 1 .4 1 1V20c0 .6-.4 1-1 1A17 17 0 0 1 3 4c0-.6.4-1 1-1h3.5c.6 0 1 .4 1 1 0 1.3.2 2.5.6 3.6.1.3 0 .7-.2 1z"/></svg></span>
    <div><strong>0123 / 732 418 0</strong><small>MO. - FR. VON 09:00 BIS 18:00 UHR</small></div>
  </div>
</header>

<nav class="nav">
  <a>Online-Shop ▾</a><a>Service ▾</a><a>Locations</a><a>For Handler</a><a>Installers</a><a>Zen</a><a>Counselor</a>
</nav>

<div class="perks">
  <span><svg width="26" height="26" viewBox="0 0 24 24"><circle cx="12" cy="12" r="7" fill="none" stroke="#fff" stroke-width="4" stroke-dasharray="3 2.5"/><circle cx="12" cy="12" r="3" fill="#fff"/></svg>Heating incl. Assembly</span>
  <span><svg width="24" height="24" viewBox="0 0 24 24"><path fill="#fff" d="M3 3h9l9 9-9 9-9-9zM7 6a1.5 1.5 0 1 0 0 3 1.5 1.5 0 0 0 0-3z"/></svg>Fixed price offer</span>
  <span><svg width="26" height="26" viewBox="0 0 24 24"><circle cx="12" cy="12" r="11" fill="#fff"/><path d="M7 12l3.5 3.5L17 9" stroke="#f78f20" stroke-width="2.6" fill="none"/></svg>Free, no-obligation</span>
  <div class="award"><div role="img" aria-label="Recommendation seal with a portrait of a chimney sweep"></div></div>
</div>

<section class="hero" role="img" aria-label="Technician installing a stainless steel chimney">
  <h1>STEEL CHIMNEY</h1>
  <p>All stainless steel chimneys made in Germany<br>with 25 years warranty.</p>
  <a class="btn">The property is offered</a>
  <span class="arrow" style="left:36px"><svg width="14" height="14" viewBox="0 0 14 14"><path d="M9 2 4 7l5 5" stroke="#fff" stroke-width="2.5" fill="none"/></svg></span>
  <span class="arrow" style="right:36px"><svg width="14" height="14" viewBox="0 0 14 14"><path d="m5 2 5 5-5 5" stroke="#fff" stroke-width="2.5" fill="none"/></svg></span>
</section>

<div class="partners">
  <span><i></i>Ferrovent</span><span><i></i>Kesselberg</span><span><i></i>Rauchwerk</span>
</div>

<section class="features">
  <div class="feature">
    <div class="circle"><svg width="44" height="50" viewBox="0 0 24 28"><path fill="#fff" d="M12 1c1 5 7 8 7 15a7 7 0 0 1-14 0c0-4 2-6 3-8 0 3 1 4 2 4 0-4 0-7 2-11z"/></svg></div>
    <h3>Mandatory heating supply<br>immediately!</h3>
    <p>On the other hand, we denounce<br>with righteous indignation and dislike<br>men who are so beguiled</p>
  </div>
  <div class="feature">
    <div class="circle"><svg width="44" height="44" viewBox="0 0 24 24"><path fill="#fff" d="M2 10h4v12H2zM8 22V10l5-8c1.5 0 2.5 1 2 3l-1 4h6c1.2 0 2 1 1.8 2.2l-1.6 8.8c-.2 1.2-1 2-2.2 2z"/></svg></div>
    <h3>More than 30 years master<br>quality!</h3>
    <p>On the other hand, we denounce<br>with righteous indignation and dislike<br>men who are so beguiled</p>
  </div>
  <div class="feature">
    <div class="circle"><svg width="46" height="46" viewBox="0 0 24 24"><circle cx="12" cy="12" r="7.5" fill="none" stroke="#fff" stroke-width="4" stroke-dasharray="3.2 2.6"/><circle cx="12" cy="12" r="4" fill="#fff"/><text x="12" y="14.5" font-size="6" font-weight="700" text-anchor="middle" fill="#f78f20" font-family="Open Sans,sans-serif">€</text></svg></div>
    <h3>New heating already from<br>39 € per month!</h3>
    <p>On the other hand, we denounce<br>with righteous indignation and dislike<br>men who are so beguiled</p>
  </div>
  <div class="feature">
    <div class="circle"><svg width="42" height="48" viewBox="0 0 24 28"><circle cx="12" cy="10" r="9" fill="#fff"/><path fill="#fff" d="M6 16 3 27l4-2 3 3 2-9zM18 16l3 11-4-2-3 3-2-9z"/><path d="M8 10l3 3 5-5" stroke="#f78f20" stroke-width="2.2" fill="none"/></svg></div>
    <h3>10 year warranty on your<br>new heater!</h3>
    <p>On the other hand, we denounce<br>with righteous indignation and dislike<br>men who are so beguiled</p>
  </div>
</section>

<section class="how" role="img" aria-label="Modern kitchen interior behind an orange overlay">
  <h2>HOW IT WORKS</h2>
  <p class="sub">In a few steps to the right property is offered for their rehabilitation</p>
  <div class="steps">
    <div class="step"><div class="ring"><span class="num">1</span><svg width="56" height="44" viewBox="0 0 28 22"><rect x="5" y="2" width="18" height="13" rx="1" fill="none" stroke="#fff" stroke-width="2"/><path d="M1 18h26l-2 3H3z" fill="#fff"/></svg></div><p>Enter Data Online</p></div>
    <div class="step"><div class="ring"><span class="num">2</span><svg width="56" height="56" viewBox="0 0 28 28"><path d="M4 24 20 4l4 4L8 28z" fill="#fff"/><path d="M4 4l20 20" stroke="#fff" stroke-width="4"/></svg></div><p>Measuring and Advice<br>by cros</p></div>
    <div class="step"><div class="ring"><span class="num">3</span><svg width="50" height="56" viewBox="0 0 24 28"><path d="M3 2h12l6 6v18H3z" fill="none" stroke="#fff" stroke-width="2"/><path d="M7 13h10M7 17h10M7 21h6" stroke="#fff" stroke-width="2"/></svg></div><p>Offer of 2 energy-hero<br>craftsmen</p></div>
    <div class="step"><div class="ring"><span class="num">4</span><svg width="58" height="52" viewBox="0 0 30 26"><circle cx="11" cy="15" r="6" fill="none" stroke="#fff" stroke-width="4" stroke-dasharray="2.6 2"/><circle cx="22" cy="7" r="4" fill="none" stroke="#fff" stroke-width="3" stroke-dasharray="2 1.6"/></svg></div><p>Execution</p></div>
  </div>
  <div class="cta"><span>Now non-binding request!</span><a class="btn">Make inquiry!</a></div>
</section>

<section class="products">
  <h2>OUR PRODUCTS</h2>
  <span class="round" style="left:60px"><svg width="10" height="12" viewBox="0 0 10 12"><path d="M7 1 2 6l5 5" stroke="#aaa" stroke-width="1.6" fill="none"/></svg></span>
  <span class="round" style="right:60px"><svg width="10" height="12" viewBox="0 0 10 12"><path d="m3 1 5 5-5 5" stroke="#aaa" stroke-width="1.6" fill="none"/></svg></span>
  <div class="grid">
    <div class="card"><div class="img" role="img" aria-label="Stainless steel chimney extension" style="background:linear-gradient(180deg,#f4f4f4,#dcdcdc)"></div><h3>Chimney Extension</h3><p>Fireplace extensions configurable produced made to measure and crafted to the highest standard.</p><div class="price">€ 63,00</div><a class="btn">Watch now</a></div>
    <div class="card"><div class="img" role="img" aria-label="Stainless steel chimney cover" style="background:linear-gradient(180deg,#f2f2f2,#d6d6d6)"></div><h3>Chimney Cover</h3><p>Fireplace covers for all chimneys purchased individually. Highest durability and quality for your chimney.</p><div class="price">€ 116.50</div><a class="btn">Watch now</a></div>
    <div class="card"><div class="img" role="img" aria-label="Wall bushing for exhaust pipes" style="background:linear-gradient(180deg,#efefef,#d2d2d2)"></div><h3>Wall bushing</h3><p>Wall penetrations for the safe conduct of exhaust pipes through walls of buildings. Fire protection at the highest level.</p><div class="price">€ 99,90</div><a class="btn">Watch now</a></div>
    <div class="card"><div class="img" role="img" aria-label="Black stovepipe elbow" style="background:linear-gradient(180deg,#f2f2f2,#cfcfcf)"></div><h3>Stovepipe</h3><p>Order stovepipes in black or gray cast in premium quality right here. Highest quality for your safety.</p><div class="price">€ 9,90</div><a class="btn">Watch now</a></div>
  </div>
</section>

<section class="seo">
  <h2>Stainless steel chimneys, chimney extensions, stovepipes and chimney accessories - at kaminwelt-versand.de buy anything cheap.</h2>
  <p>Can I use a steel chimney for sale on the Internet? This question you have probably never asked. For other products which is a matter of course, but with a stainless steel chimney you do not think first to the online shopping. There are the all around the subject for several years various platforms steel chimney offer. However, these providers operate their web shop only incidentally. This is reflected in the poor usability and the partly very outdated technology of pages. Kaminwelt Versand has gone a new way here. The goal was a pet shop for stainless steel chimneys and chimney accessories to put on their feet, which is composed not only professionally and according to the latest state of the art, but also gives you the security and usability that you are used to large online platforms in other sectors. With an efficient organization, modern technology and years of experience with the product steel chimney, this claim could be met. Best usability, certified privacy, quality products and expert advice by telephone round your shopping experience from Kaminwelt Versand.</p>
  <h3>Steel chimney, chimney kit and stainless steel chimney - all from one source.</h3>
  <p>Whether you have a double-walled stainless steel chimney, a chimney restoration looking for your old brick fireplace or chimney kit for your home: here you will find it. In Kaminwelt Versand you can find a wide range of manufactured in Germany stainless steel chimneys from our partner Ferrovent. These chimneys are manufactured according to the latest production methods of high-quality V4A stainless steel and are subject to stringent quality specifications. The manufacturer gives you beyond a guarantee of 25 years on each steel chimney acquired in this online shop. Quite simply: security at the best price!</p>
  <p>And another tip: All chimneys can be wonderfully with a stovepipe connect. Here there is a large range of variants, lengths, colors and angles. In addition, more recently, insulated stovepipes are available. This double-walled furnace tubes reduce the distance that must be maintained to combustible materials to a minimum.</p>
  <h3>Build chimney extension and cowl extension low self.</h3>
  <p>Due to new regulations, the height of many existing chimneys is no longer enough. By structural changes in the environment or many other reasons, it may happen that a chimney extension is necessary. In this online store you will find chimney extensions in versions double or single wall. Each chimney extension is made by hand and can be configured exactly to measure. Here you buy a chimney extension for eternity.</p>
  <h3>Lightweight construction chimney F90 and a wall duct: fire protection at the highest level.</h3>
  <p>A stainless steel chimney is an excellent subsequent exhaust pipe beside an already brick chimney in the building. But what if you do not like the look or you prefer to leave the chimney inside invisible disappear? But that is lightweight engineering chimney preselected. In conjunction with a refractory wall bushing here you have the perfect duo for secure additional chimney.</p>
  <h3>Chimney cap, chimney cover and chimney cover plate stainless steel to measure.</h3>
  <p>Older chimney heads are subject to heavy loads due to weather conditions. After many years of rain, sunshine, the cold and the heat chimney tops are porous and begin to crumble. Then it is high time for a chimney cover plate and a chimney cowl. In fireplace covers, there are the well known hood and ridge styles. These models have proven themselves over many years and are also mounted on most buildings. In this shop we offer chimney covers made of stainless steel or copper with 25 years warranty.</p>
  <h3>Chimney fans, draft stabilizer, fire doors and other specialty products</h3>
  <p>Record this online shop you will also find many other products around the topic of chimney and exhaust technology. Here for example, would the chimney fan to call. A very important device, which allows you to increase the chimney draft electrically. Also from the category of tension control and draft adjustment there is the draft regulator. These so-called secondary air devices regulate purely mechanical chimney draft. In some cases, may also include a flue gas damper are necessary. In addition to the thermal exhaust flap can be found here also motorized flue dampers, which may be necessary for cascade in chimneys with double occupancy. Is finally even the fireplace door to mention. This component have most of them installed in the chimney side. Find suitable replacement, it should be ever rusted.</p>
  <p>Enjoy shopping, wishes you the team of Kaminwelt Versand.</p>
</section>

<footer class="footer">
  <div class="cols">
    <div class="brand light"><span class="mark"></span><span class="name">Kaminwelt<br>Versand</span></div>
    <div class="col-info"><h4>Information</h4><ul><li>FAQ</li><li>About Us</li><li>Conditions</li><li>Revocation</li><li>Delivery</li><li>Data Protection</li><li>Contact us</li></ul></div>
    <div class="col-news"><h4>Newsletter Subscription</h4><p>Register Your Email Address to get<br>information about us</p><div class="field">Email Address</div><a class="btn">Subscribe</a></div>
    <div class="col-contact"><h4>Contact Us</h4><ul>
      <li><svg width="10" height="13" viewBox="0 0 10 13"><path fill="#fff" d="M5 0a5 5 0 0 0-5 5c0 4 5 8 5 8s5-4 5-8a5 5 0 0 0-5-5zm0 7a2 2 0 1 1 0-4 2 2 0 0 1 0 4z"/></svg><span>Lindenweg 14<br>80331 Munich<br>Germany</span></li>
      <li><svg width="11" height="11" viewBox="0 0 24 24"><path fill="#fff" d="M6.6 10.8a15 15 0 0 0 6.6 6.6l2.2-2.2c.3-.3.7-.4 1-.2 1.1.4 2.3.6 3.6.6.6 0 1 .4 1 1V20c0 .6-.4 1-1 1A17 17 0 0 1 3 4c0-.6.4-1 1-1h3.5c.6 0 1 .4 1 1 0 1.3.2 2.5.6 3.6.1.3 0 .7-.2 1z"/></svg><span>0123/732 418 0</span></li>
      <li><svg width="12" height="10" viewBox="0 0 12 10"><rect width="12" height="10" rx="1" fill="#fff"/><path d="M0 1l6 5 6-5" stroke="#262626" fill="none"/></svg><span>info@kaminwelt-versand.de</span></li>
    </ul></div>
  </div>
  <div class="bottom">
    <span>© 2016, Kaminwelt Versand. All rights reserved.</span>
    <div class="pay"><span>Plenvo</span><span>Payvo</span><span>Cashlo</span><span>Bankly</span><span>Invoio</span></div>
    <div class="social"><i></i><i></i><i></i></div>
  </div>
</footer>

</body>
</html>
```